VARQO Business card

Black card, double sided with company colors black, blue and white with slogan on back Your VARQO......

Industry/Entity Type

Business

```html
<!DOCTYPE html>
<html lang="en">
<head>
<meta charset="utf-8">
<title>VARQO Business Card</title>
<link href="https://fonts.googleapis.com/css2?family=Open+Sans:wght@400;600&display=swap" rel="stylesheet">
<style>
  :root {
    --stage-top: #d9d9d9;
    --stage-bottom: #f6f6f6;
    --card-white: #ffffff;
    --brand-blue: #2aa7df;
    --ink: #1c1c1c;
    --back-deep: #0c3540;
    --back-mid: #116475;
    --back-bright: #1fb0d6;
    --slogan: #f2f7f9;
  }
  * { box-sizing: border-box; margin: 0; padding: 0; }
  html, body {
    width: 1200px;
    height: 900px;
    overflow: hidden;
  }
  body {
    background: linear-gradient(180deg, var(--stage-top) 0%, var(--stage-bottom) 70%);
    font-family: "Open Sans", Arial, sans-serif;
    position: relative;
  }
  .card {
    position: absolute;
    top: 300px;
    width: 520px;
    height: 300px;
    border-radius: 28px;
    overflow: hidden;
    box-shadow: 0 18px 30px rgba(0, 0, 0, 0.18);
  }
  .card-front {
    left: 50px;
    background: var(--card-white);
  }
  .card-back {
    left: 630px;
    background: linear-gradient(110deg, var(--back-deep) 0%, var(--back-mid) 55%, var(--back-bright) 100%);
  }
  .brand {
    position: absolute;
    left: 30px;
    top: 34px;
    display: flex;
    align-items: center;
    gap: 10px;
  }
  .brand-dot {
    width: 30px;
    height: 30px;
    border-radius: 50%;
    background: var(--brand-blue);
  }
  .brand-name {
    font-size: 40px;
    font-weight: 600;
    color: var(--brand-blue);
    letter-spacing: 1px;
  }
  .contact-list {
    position: absolute;
    left: 28px;
    bottom: 30px;
    list-style: none;
    font-size: 14px;
    line-height: 19px;
    color: var(--ink);
  }
  .contact-list li {
    display: flex;
    align-items: center;
    gap: 6px;
  }
  .contact-icon {
    width: 13px;
    height: 13px;
    fill: var(--brand-blue);
  }
  .slogan {
    position: absolute;
    left: 32px;
    top: 34px;
    font-size: 21px;
    letter-spacing: 7px;
    color: var(--slogan);
    z-index: 2;
  }
  .back-pattern {
    position: absolute;
    inset: 0;
    background:
      radial-gradient(ellipse at 90% 60%, rgba(60, 200, 235, 0.55) 0%, rgba(31, 176, 214, 0.25) 40%, rgba(12, 53, 64, 0) 75%);
  }
</style>
</head>
<body>

  <section class="card card-front" aria-label="Card front">
    <div class="brand">
      <span class="brand-dot"></span>
      <span class="brand-name">VARQO</span>
    </div>
    <ul class="contact-list">
      <li>
        <svg class="contact-icon" viewBox="0 0 16 16"><rect x="4" y="1" width="8" height="14" rx="1.5"/></svg>
        2740 318 506
      </li>
      <li>
        <svg class="contact-icon" viewBox="0 0 16 16"><path d="M3 1l3 0 1 4-2 1.5c1 2 2.5 3.5 4.5 4.5L11 9l4 1v3c0 1-1 2-2 2C7 15 1 9 1 3c0-1 1-2 2-2z"/></svg>
        6391 207 845
      </li>
      <li>
        <svg class="contact-icon" viewBox="0 0 16 16"><rect x="1" y="6" width="14" height="9" rx="1.5"/><rect x="4" y="1" width="8" height="6"/></svg>
        6173 592 430
      </li>
      <li>
        <svg class="contact-icon" viewBox="0 0 16 16"><path d="M1 3h14v10H1z M1 3l7 6 7-6" stroke="#fff" stroke-width="1"/></svg>
        hello@varqostudio.com
      </li>
      <li>
        <svg class="contact-icon" viewBox="0 0 16 16"><circle cx="8" cy="8" r="7"/><path d="M1 8h14M8 1c-3 4-3 10 0 14M8 1c3 4 3 10 0 14" stroke="#fff" stroke-width="1" fill="none"/></svg>
        www.varqostudio.com
      </li>
      <li>
        <svg class="contact-icon" viewBox="0 0 16 16"><path d="M8 1L1 8h2v7h4v-4h2v4h4V8h2z"/></svg>
        14 Harbour Lane, Sydney, NSW 2000
      </li>
    </ul>
  </section>

  <section class="card card-back" aria-label="Card back">
    <p class="slogan">Your VARQO......</p>
    <div class="back-pattern" role="img" aria-label="Receding field of round brand-symbol buttons in teal and cyan"></div>
  </section>

</body>
</html>
```